Packaging Design - Labels for Organic Body Care Range

I am re-designing the current range of our Body Care Skin Care range.

It is a range of natural and organic skin care with 5 products.

The range is currently very girly and young look but we are opting for a more of a raw, edgy, organic look so that we will be well definited as being organic.

I am attaching the Design file of the the current packaging.

I have recently used Pixel Forge to redesign our baby range and the beige background design was the one chosen:

http://www.pixelforgeo.net/project-progress.aspx?briefId=58316&show=designs So something along these lines will be preferred so that it all goes together.

Have included some design inspiration below.

Look forward to seeing your designs.
Updates

I have updated the brief and included some design inspiration for these designs.

Hope this helps

Target Market(s)

Women 25 - 50 yrs

Industry/Entity Type

Baby

Requirements
Must have
• Natural feel
organic feel
Textured look
Eco chic
Luxury feel
Boutique feel
Nice to have
• bright colours
Sutble Floral (see example designs)
Should not have
• No minimilist designs ie Marbo, Tyvan etc
No Purple, Blue, or green
Avoid too much pink

```html
<!DOCTYPE html>
<html lang="en">
<head>
<meta charset="utf-8">
<title>Wholly Radiant Essentials – Healing Hands &amp; Nails Cream Label</title>
<link rel="stylesheet" href="https://fonts.googleapis.com/css2?family=Jost:ital,wght@0,300;0,400;1,300&family=Pathway+Gothic+One&family=Poiret+One&family=Arimo:wght@700&family=Oswald:wght@300&display=swap">
<style>
  :root {
    --kraft-light: #c98a3e;
    --kraft-mid: #b8742b;
    --kraft-dark: #9a5e22;
    --ink: #2a2620;
    --ink-deep: #1c1a14;
    --label-navy: #161821;
    --label-gold: #b88a4e;
    --label-cream: #d9c7ae;
    --title-rose: #c2446a;
    --ingredient-grey: #6e6a66;
    --blossom-red: #ff3355;
  }
  * { margin: 0; padding: 0; box-sizing: border-box; }
  html, body { width: 1200px; height: 915px; overflow: hidden; }
  body {
    position: relative;
    background:
      radial-gradient(ellipse at 30% 40%, rgba(255,220,150,0.25), transparent 60%),
      radial-gradient(ellipse at 80% 85%, rgba(90,45,10,0.25), transparent 55%),
      linear-gradient(160deg, var(--kraft-light) 0%, var(--kraft-mid) 55%, var(--kraft-dark) 100%);
    color: var(--ink);
  }

  /* Back panel */
  .cert-badges { position: absolute; left: 80px; top: 55px; display: flex; gap: 34px; }
  .cert-badge { width: 72px; height: 72px; border-radius: 50%; border: 3px solid var(--ink-deep); }

  .description {
    position: absolute; left: 53px; top: 172px; width: 365px;
    font-family: "Jost", sans-serif; font-weight: 300; font-size: 18px; line-height: 24.6px;
    text-align: justify; color: var(--ink);
  }
  .directions {
    position: absolute; left: 53px; top: 466px; width: 365px;
    font-family: "Pathway Gothic One", sans-serif; font-size: 18px; line-height: 24.6px;
    text-align: justify; color: var(--ink-deep);
  }
  .maker {
    position: absolute; left: 53px; top: 809px;
    font-family: "Arimo", sans-serif; font-weight: 700; font-size: 14px; line-height: 17px;
    color: var(--ink-deep);
  }
  .shelf-life { position: absolute; left: 338px; top: 803px; width: 64px; height: 60px; }

  /* Front panel */
  .blossom-frame { position: absolute; left: 478px; top: 22px; width: 660px; height: 780px; }

  .front-label {
    position: absolute; left: 640px; top: 165px; width: 326px; height: 525px;
    background: var(--label-navy); border-radius: 163px;
  }
  .front-label::after {
    content: ""; position: absolute; inset: 7px;
    border: 1.5px solid var(--label-gold); border-radius: 156px;
  }
  .brand {
    position: absolute; top: 106px; width: 100%; text-align: center;
    font-family: "Jost", sans-serif; font-weight: 300; color: var(--label-gold);
    letter-spacing: 0.5px; line-height: 25px;
  }
  .brand-name { font-size: 17px; display: block; }
  .brand-line { font-size: 20px; display: block; }
  .product-name {
    position: absolute; top: 216px; width: 100%; text-align: center;
    font-family: "Poiret One", sans-serif; font-size: 31px; line-height: 34px;
    color: var(--title-rose); font-variant: small-caps; letter-spacing: 1px;
  }
  .ingredients {
    position: absolute; top: 362px; left: 24px; right: 24px; text-align: center;
    font-family: "Jost", sans-serif; font-style: italic; font-weight: 300;
    font-size: 15px; line-height: 22px; color: var(--ingredient-grey);
  }
  .scent {
    position: absolute; left: 748px; top: 784px;
    font-family: "Oswald", sans-serif; font-weight: 300; font-style: italic;
    font-size: 24px; line-height: 24px; color: var(--ink-deep); font-variant: small-caps;
    transform: skewX(-8deg);
  }
  .scent span { display: block; }
  .scent span + span { padding-left: 14px; }
  .volume {
    position: absolute; left: 748px; top: 860px;
    font-family: "Oswald", sans-serif; font-weight: 300; font-size: 19px;
    color: var(--ink-deep); transform: skewX(-8deg);
  }
</style>
</head>
<body>

  <section class="back-panel">
    <div class="cert-badges">
      <div class="cert-badge" aria-label="Australian made badge"></div>
      <div class="cert-badge" aria-label="Certified organic badge"></div>
      <div class="cert-badge" aria-label="No animal testing badge"></div>
    </div>

    <p class="description">Lorem ipsum dolor sit amet, consectetur adipiscing elit. Sed non risus. Suspendisse lectus tortor, dignissim sit amet, adipiscing nec, ultricies sed, dolor. Cras elementum ultrices diam. Maecenas ligula massa, varius a, semper congue, euismod non, mi. Proin porttitor, orci nec nonummy molestie, enim est eleifend mi, non fermentum diam nisl sit amet erat.</p>

    <p class="directions">Duis semper. Duis arcu massa, scelerisque vitae, consequat in, pretium a, enim. Pellentesque congue. Ut in risus volutpat libero pharetra tempor. Cras vestibulum bibendum augue. Praesent egestas leo in pede. Praesent blandit odio eu enim. Pellentesque sed dui ut augue blandit sodales. Vestibulum ante ipsum primis in faucibus orci luctus et ultrices posuere cubilia Curae; Aliquam nibh. Mauris ac mauris sed pede pellentesque fermentum. Maecenas adipiscing ante non diam sodales hendrerit.</p>

    <p class="maker">Made in Australia<br>Wholly Radiant<br>www.whollyradiant.com.au</p>

    <svg class="shelf-life" viewBox="0 0 64 60" aria-label="Use within 12 months of opening">
      <path d="M6 14 L52 2 L54 8 L8 20 Z" fill="none" stroke="#1c1a14" stroke-width="3" stroke-linejoin="round"/>
      <path d="M6 24 H58 V52 Q58 58 52 58 H12 Q6 58 6 52 Z" fill="none" stroke="#1c1a14" stroke-width="3"/>
      <text x="32" y="48" text-anchor="middle" font-family="Arimo, sans-serif" font-weight="700" font-size="14" fill="#1c1a14">12M</text>
    </svg>
  </section>

  <section class="front-panel">
    <svg class="blossom-frame" viewBox="0 0 660 780" role="img" aria-label="Red line-drawn floral ornament of lavender sprigs and mandarin blossoms framing the label">
      <defs>
        <radialGradient id="blossomGlow" cx="50%" cy="48%" r="50%">
          <stop offset="0%" stop-color="#ff3355" stop-opacity="0.35"/>
          <stop offset="70%" stop-color="#ff3355" stop-opacity="0.18"/>
          <stop offset="100%" stop-color="#ff3355" stop-opacity="0"/>
        </radialGradient>
      </defs>
      <ellipse cx="330" cy="390" rx="330" ry="390" fill="url(#blossomGlow)"/>
    </svg>

    <div class="front-label">
      <h1 class="brand">
        <span class="brand-name">WHOLLY RADIANT</span>
        <span class="brand-line">ESSENTIALS</span>
      </h1>
      <h2 class="product-name">Healing hands<br>&amp; nails cream</h2>
      <p class="ingredients">contains an organic herbal blend, infused with organic shea butter, rosehip oil &amp; jojoba seed oil</p>
    </div>

    <p class="scent"><span>Lavender &amp;</span><span>Mandarin</span></p>
    <p class="volume">100ml / 3.4 fl oz</p>
  </section>

</body>
</html>
```